Banner Ad Design Project

I need a banner design. The website is under construction at www.brightmarrow.example

Name: Bright Marrow
Tagline: Steady Sparks for crowded calendars

This is a leadership development and executive coaching site. The past site is live at www.quillstepnow.example. (so you can get a sense of the content)

The audience are (BUSY) executives, senior managers, leaders and top professionals, so the feel needs to be highly professional but also modern and fresh. I want to communicate energy but also solid and trust worthy and not too new agey. The audience are also people with strong social values who want to change things - so not too corporate (Ie suits!)

I would like the design to be floating on a white background, very clean and simple. I am attracted to reds or sunset (burn orange crimson colors.) But totally open to any color ideas.
I am giving an open brief for your ideas.
Here are the dimensions 960px wide, roughly 190px height.

Reason: The weekend might give more time to designers to get involved. Thanks Vina

Hi designers

You may not have seen the additions I gave to this brief.

The banner should not have leader out front photo's. Maybe less corporate than I initially thought. 
Not too corporate (no suits!) Please no chess pieces, jigsaw pieces, cartoon images, cliche leadership images. 
Am am trying for inspiration /inspiring whilst still being professional. Very simple and clean.
Please can the design be floating in a white background so that the web page is borderless - A bit like it is in http://palmoriskel.example/
Thank you

Target Market(s)

Senior managers, executives but people who also want to change the world!

Industry/Entity Type

Construction

Requirements
Should not have
• Should not have leader out front photo's.
Maybe less corporate than I initially thought.
Am am trying for inspiration /inspiring whilst still being professional.
Please no chess pieces, jigsaw pieces, cartoon images, cliche leadership images. Not too corporate (Ie suits!)

Thanks

```html
<!DOCTYPE html>
<html lang="en">
<head>
<meta charset="utf-8">
<title>Bright Marrow — Steady Sparks for crowded calendars</title>
<link rel="stylesheet" href="https://fonts.googleapis.com/css2?family=Cinzel:wght@500&family=Open+Sans:wght@400&display=swap">
<style>
  :root {
    --ember: #ea5a12;
    --ember-soft: #f7a26a;
    --peach: #fbd9bd;
    --cream: #fff7f0;
    --paper: #ffffff;
    --bark: #3b1f14;
    --wood: #e2bf85;
    --lead-red: #d9261c;
  }
  html, body {
    margin: 0;
    padding: 0;
    overflow: hidden;
    background: var(--paper);
  }
  .banner {
    position: relative;
    width: 1200px;
    height: 238px;
    overflow: hidden;
    background:
      radial-gradient(ellipse 520px 60px at 30% 132px, rgba(247,162,106,0.45), rgba(255,255,255,0) 70%),
      radial-gradient(ellipse 900px 40px at 55% 232px, rgba(234,90,18,0.45), rgba(255,255,255,0) 75%),
      linear-gradient(180deg, var(--paper) 0%, var(--cream) 45%, var(--peach) 58%, var(--cream) 70%, var(--paper) 85%, var(--peach) 100%);
  }
  .brand {
    position: absolute;
    left: 64px;
    top: 52px;
    width: 480px;
  }
  .brand-name {
    margin: 0;
    font-family: "Cinzel", serif;
    font-weight: 500;
    font-size: 56px;
    line-height: 1;
    letter-spacing: 1px;
    color: var(--ember);
    white-space: nowrap;
  }
  .brand-rule {
    display: block;
    margin: 12px 0 0;
    width: 474px;
    height: 2px;
    background: var(--ember);
  }
  .brand-tagline {
    margin: 10px 0 0;
    font-family: "Open Sans", sans-serif;
    font-size: 17px;
    letter-spacing: 1.6px;
    text-transform: uppercase;
    color: var(--bark);
    white-space: nowrap;
  }
  .pencil-art {
    position: absolute;
    right: 0;
    top: 0;
    width: 420px;
    height: 238px;
    background:
      radial-gradient(ellipse 90px 60px at 48% 42%, rgba(217,38,28,0.85), rgba(217,38,28,0) 75%),
      linear-gradient(125deg, rgba(255,255,255,0) 12%, var(--wood) 45%, #f0d7a8 70%, var(--wood) 100%);
    -webkit-mask-image: linear-gradient(90deg, transparent 0%, #000 30%);
    mask-image: linear-gradient(90deg, transparent 0%, #000 30%);
  }
</style>
</head>
<body>
  <header class="banner">
    <div class="brand">
      <h1 class="brand-name">Bright Marrow</h1>
      <span class="brand-rule"></span>
      <p class="brand-tagline">Steady Sparks for crowded calendars</p>
    </div>
    <div class="pencil-art" role="img" aria-label="A fan of sharpened wooden pencils pointing up-left, one red pencil standing out among the natural wood ones"></div>
  </header>
</body>
</html>
```